Web Design Project for accounting firm

Hi winners
we are a chartered accountancy firm. We do really want to get into SEO. The link below is to our current website which I don't really like as it looks too simple.
www.qmledgerwise.com.au
In the homepage
I want to have Service tab, Testimonial tab, Events tab, Partner tab, blog tab and contact us tab
I want to have a section which have a bit description of the rencent blog and by clicking the section,you get into the real blogging page
I want a section which shows the most current client testimonials and by click into it, it gives you the testimonial page
I want a section for service which have a discription of the service overall and once click into more details, service details page pop up
I want a section for parter which had a bit description of the partner and linked to the detailed partner page
a section shows the contact number
a section for social media
a section for my logos, a section for QG logo and a section says "Liability limited by a scheme approved under Professional Standards Legislation"
In the first round, everyone can just design the homepage for me. And I will pick a couple for the second round to design the service page. and then I pick one to finish off the whole web design project.
below are the website I am planning to get
http://www.tallowmere.com.au/
http://www.brightpathledgers.com.au/ (my favourate)
Here is the link to download the QG logo
http://www.qualifiedtallyguild.com.au/Members/Marketing-your-practice/Logos
Updates
Hi Guys
I have reloaded the attachments. Hopefully works this time
I also add the link to the QG logo since someone has just asked
Will guarantee the payment when something good comes up. Won't wait until the due date.
Hi designers
I have guaranteed the payment. I am open to any good design now.
Marta

```html
<!DOCTYPE html>
<html lang="en">
<head>
<meta charset="utf-8">
<title>QM Ledgerwise Accounting Services – Our Partners</title>
<link href="https://fonts.googleapis.com/css2?family=PT+Sans:wght@400;700&family=PT+Sans+Narrow:wght@700&display=swap" rel="stylesheet">
<style>
:root{
  --page:#ffffff;
  --page-top:#e9e9e9;
  --red:#8c0d0d;
  --ink:#444444;
  --ink-soft:#555555;
  --muted:#9a9a9a;
  --panel:#f0f0f0;
  --panel-head:#dedede;
  --rule:#d6d6d6;
  --nav-top:#4a4a4a;
  --nav-bottom:#0c0c0c;
  --footer-top:#5b5b5b;
  --footer-bottom:#2f2f2f;
}
*{box-sizing:border-box;margin:0;padding:0}
html,body{width:1200px;height:953px;overflow:hidden}
body{position:relative;background:linear-gradient(var(--page-top),var(--page) 130px);font-family:"PT Sans",sans-serif;color:var(--ink)}
.abs{position:absolute}

/* header */
.brand{left:141px;top:28px;display:flex;align-items:center;gap:14px}
.brand-mark{width:46px;height:46px;background:var(--red)}
.brand-name{font-size:27px;letter-spacing:2px;color:#333;font-weight:400;text-transform:uppercase}
.call{left:818px;top:35px;width:241px;height:45px;border-top:1px solid #c4c4c4;border-bottom:1px solid #c4c4c4;display:flex;align-items:center;gap:14px;padding-left:10px}
.call-icon{width:24px;height:24px;border-radius:4px;background:#9c9c9c;display:flex;align-items:center;justify-content:center}
.call-text{font-family:"PT Sans Narrow",sans-serif;font-weight:700;font-size:22px;color:#555}

/* navigation */
.nav{left:141px;top:105px;width:918px;height:50px;background:linear-gradient(var(--nav-top),var(--nav-bottom));display:flex;align-items:stretch}
.nav a{color:#b9b9b9;text-decoration:none;font-size:15px;display:flex;align-items:center;padding:0 14px;border-right:1px solid #222;text-transform:uppercase}
.nav a:first-child{padding-left:27px}
.nav a.current{background:linear-gradient(#e2332b,#b9140f);color:#fff;font-weight:700}
.search{position:absolute;left:673px;top:12px;width:227px;height:24px;background:#fff;border:1px solid #999;font-size:10px;color:#777;padding:6px 8px}
.search svg{position:absolute;right:6px;top:4px}

/* section headings */
.head{height:40px;background:#f3f3f3;border:1px solid #e2e2e2;display:flex;align-items:center;padding-left:12px;gap:13px;font-size:19px;color:var(--red)}
.ribbon{width:19px;height:30px;background:var(--red);clip-path:polygon(0 0,100% 0,100% 100%,50% 78%,0 100%);margin-top:-8px}

/* services */
.services-head{left:143px;top:178px;width:206px}
.service-list{left:166px;top:236px;list-style:none;font-size:12px;color:var(--ink-soft)}
.service-list li{height:26.25px}

/* partner */
.partner-head{left:357px;top:178px;width:429px}
.partner-col{left:366px;top:229px;width:416px}
.partner-name{font-size:15px;line-height:20px;height:24px;color:#555}
.photo{float:left;width:119px;height:150px;margin:0 6px 4px -2px;border:1px solid #bbb;background:linear-gradient(#ece9e4,#c9b8a6 55%,#e7e1d8)}
.sub{font-size:13px;font-weight:700;color:var(--red)}
.exp-title{line-height:17px}
.exp-body{font-size:11.5px;line-height:22.5px;text-align:justify;hyphens:auto;-webkit-hyphens:auto;color:var(--ink)}
.exp-end{clear:both}
.expertise-title{margin-top:14px;line-height:17px}
.expertise{list-style:none;font-size:12px;color:var(--ink-soft);margin:10px 0 0 12px}
.expertise li{height:21.6px;display:flex;align-items:flex-start;gap:11px}
.expertise li::before{content:"";width:0;height:0;border-left:4px solid #666;border-top:4px solid transparent;border-bottom:4px solid transparent;margin-top:4px}
.qual-title{margin:4px 0 0 4px;line-height:17px}
.quals{list-style:none;font-size:13px;color:var(--ink-soft);margin:6px 0 0 6px}
.quals li{height:20.6px}

/* sidebar */
.side{left:795px;width:257px;background:var(--panel)}
.side-head{height:36px;background:var(--panel-head);font-size:18px;color:var(--red);padding:8px 16px}
.blog{top:179px;height:318px}
.post{margin:0 11px;padding:12px 6px 9px;border-bottom:1px solid var(--rule);font-family:Arial,sans-serif}
.post:last-child{border-bottom:0}
.post-title{display:flex;gap:8px;align-items:center;font-family:"PT Sans",sans-serif;font-size:12.5px;color:#555}
.meta{font-family:"PT Sans",sans-serif;font-style:italic;font-size:10px;color:#555;margin:6px 0 8px}
.excerpt{font-size:11px;line-height:18.75px;color:var(--muted);text-align:justify}
.more{text-align:right;font-size:12px;color:#555;margin-top:1px;padding-right:6px}
.testimonials{top:504px;height:272px}
.quote{margin:0 11px;padding:12px 0 8px;border-bottom:1px solid var(--rule);display:flex;gap:9px}
.avatar{width:52px;height:52px;flex:none;border:3px solid #fff;box-shadow:0 0 2px #999;background:linear-gradient(#6aa0c8,#c79a80)}
.quote-text{font-family:Arial,sans-serif;font-size:12px;line-height:18.75px;color:var(--muted);text-align:justify}
.quote-meta{text-align:right;font-style:italic;font-size:10.5px;color:#555;margin-top:3px}

/* footer */
.footer{left:0;top:850px;width:1200px;height:103px;background:linear-gradient(var(--footer-top),var(--footer-bottom))}
.follow{left:856px;top:850px;width:203px;height:26px;background:#e6e6e6;display:flex;align-items:center;gap:6px;padding-left:15px;font-size:9.5px;color:#555}
.follow span{margin-right:18px}
.follow i{width:19px;height:18px;border-radius:3px;background:#8a8a8a;display:block}
.standards{left:147px;top:866px;width:267px;height:72px}
.standards-frame{position:absolute;left:38px;top:10px;right:0;bottom:3px;border:1px solid #a31b17;border-radius:4px}
.standards-badge{position:absolute;left:0;top:0;width:75px;height:75px;border-radius:50%;background:radial-gradient(circle at 40% 35%,#d63a32,#8c0d0d)}
.standards-text{position:absolute;left:81px;top:18px;font-size:12px;line-height:14px;color:#fff;text-transform:uppercase}
.copyright{left:812px;top:887px;font-size:12px;color:#e8e8e8}
</style>
</head>
<body>

<header>
  <div class="abs brand"><div class="brand-mark"></div><div class="brand-name">QM Ledgerwise Accounting Services</div></div>
  <div class="abs call">
    <div class="call-icon"><svg width="14" height="16" viewBox="0 0 14 16"><path d="M3 1 L5 1 L6 5 L4.5 6.5 Q6 10 8.5 11.5 L10 10 L13 11 L13 14 Q11 16 7 13 Q2 9 1.5 4 Q1.5 2 3 1Z" fill="#fff"/></svg></div>
    <div class="call-text">CALL : (02) 5550 1482</div>
  </div>
</header>

<nav class="abs nav">
  <a href="#">Home</a><a href="#">Services</a><a href="#">Testimonials</a><a href="#">Events</a><a href="#" class="current">Partner</a><a href="#">Blog</a><a href="#">Contact Us</a>
  <div class="search">SEARCH<svg width="16" height="16" viewBox="0 0 16 16"><circle cx="6.5" cy="6.5" r="5" fill="none" stroke="#333" stroke-width="2"/><line x1="10" y1="10" x2="15" y2="15" stroke="#333" stroke-width="2.4"/></svg></div>
</nav>

<section>
  <div class="abs head services-head"><div class="ribbon"></div>Services</div>
  <ul class="abs service-list">
    <li>Tax Accounting</li><li>Book keeping</li><li>Payroll Support</li><li>Advisory/CFO</li><li>Cloud Accounting Comparisions</li><li>Cloud Accounting Setup</li><li>Cloud Accounting Support</li><li>IT Support</li><li>Custom Services</li>
  </ul>
</section>

<main>
  <div class="abs head partner-head"><div class="ribbon"></div>Our Partners</div>
  <div class="abs partner-col">
    <div class="partner-name">Partners name</div>
    <div class="photo" role="img" aria-label="Portrait photo of the partner"></div>
    <div class="sub exp-title">Experience</div>
    <p class="exp-body">On the other hand, we denounce with righteous indignation and dislike men who are so beguiled and demoralized by the charms of pleasure of the moment, so blinded by desire, that they cannot foresee the pain and trouble that are bound to ensue; and equal blame belongs to those who fail in their duty through weakness of will, which is desire, that they cannot foresee the pain and trouble that are bound to ensue; and equal blame belongs to those who fail in their duty through weakness of will, which is the same as saying through shrinking from toil and pain. These cases are perfectly simple and easy to distinguish</p>
    <div class="exp-end"></div>
    <div class="sub expertise-title">Expertise</div>
    <ul class="expertise">
      <li>Business Services</li><li>Cashflow Management</li><li>Estate Planning</li><li>Management Accounting</li><li>Succession Planning</li><li>Superannuation</li><li>Tax Planning and Structuring</li><li>Valuations</li><li>Wealth Creation</li>
    </ul>
    <div class="sub qual-title">Qualifications</div>
    <ul class="quals"><li>Bachelor of Business</li><li>Chartered Accountant</li><li>Fellow Tax Institute</li></ul>
  </div>
</main>

<aside>
  <div class="abs side blog">
    <div class="side-head">Most Recent Blog</div>
    <div class="post">
      <div class="post-title"><svg width="17" height="17" viewBox="0 0 17 17"><rect x="1" y="3" width="13" height="13" fill="none" stroke="#aaa" stroke-width="1.5"/><path d="M7 10 L15 2" stroke="#aaa" stroke-width="2"/></svg>voluptate velit nihil molestiae</div>
      <div class="meta">Posted by : Daniel on Jan 25<sup>th</sup></div>
      <p class="excerpt">Nemo enim ipsam voluptatem quia voluptas sit aspernatur aut odit aut fugit, sed quia dolores eos qui ratione</p>
      <div class="more">View more</div>
    </div>
    <div class="post">
      <div class="post-title"><svg width="17" height="17" viewBox="0 0 17 17"><rect x="1" y="3" width="13" height="13" fill="none" stroke="#aaa" stroke-width="1.5"/><path d="M7 10 L15 2" stroke="#aaa" stroke-width="2"/></svg>voluptate velit nihil molestiae</div>
      <div class="meta">Posted by : Daniel on Jan 25<sup>th</sup></div>
      <p class="excerpt">Nemo enim ipsam voluptatem quia voluptas sit aspernatur aut odit aut fugit, sed quia dolores eos qui ratione</p>
      <div class="more">View more</div>
    </div>
  </div>

  <div class="abs side testimonials">
    <div class="side-head">Testimonials</div>
    <div class="quote">
      <div class="avatar" role="img" aria-label="Client portrait photo"></div>
      <div><p class="quote-text">Nemo enim ipsam voluptatem quia voluptas sit aspernatur aut odit aut fugit, sed quia dolores eos qui ratione</p><div class="quote-meta">Posted by : Daniel on Jan 25<sup>th</sup></div></div>
    </div>
    <div class="quote">
      <div class="avatar" role="img" aria-label="Client portrait photo"></div>
      <div><p class="quote-text">Nemo enim ipsam voluptatem quia voluptas sit aspernatur aut odit aut fugit, sed quia dolores eos qui ratione</p><div class="quote-meta">Posted by : Daniel on Jan 25<sup>th</sup></div></div>
    </div>
  </div>
</aside>

<footer>
  <div class="abs footer"></div>
  <div class="abs follow"><span>FOLLOW US :</span><i></i><i></i><i></i><i></i></div>
  <div class="abs standards">
    <div class="standards-frame"></div>
    <div class="standards-badge"></div>
    <div class="standards-text">Liability limited by a scheme<br>approved under profes-<br>sional standards legislation</div>
  </div>
  <div class="abs copyright">Copyright © 2012 QM Ledgerwise Accounting Services</div>
</footer>

</body>
</html>
```